2 stickers business card size and car sticker

design stickers for a 1300 phone number. 1 x 90mm x 42mm and the other 190mm x 50mm

The smaller art 90x42 will also be used for web and print the larger 190mm x 50mm will be used for print on a car bumper sticker. All final submissions should be original full photoshop files or illustrator files and include any font required.

The aim is to promote a 1300 phone number: 1300BLUEFOX

1300BLUEFOX should be the main attention grabber but also the actual phone number should also appear in small 1300 482 615

There can also be a secondary main attention word or words: CALL or CALL NOW and the web site 1300BLUEFOX.COM

You may also include a graphic such as a phone or other icon type graphic.

The small stickers 90x42 are to remind people of the number that will be stuck on desks, books, computers etc and also the bumper sticker.

2 examples of a smaller sticker are attached and are named example1 and example 2 .. but do not represent any style guide just a rough example of the type of ideas we are aiming for .. different ideas welcomed. I have also uploaded a bit of a fun graphic called "freefall_person" if people want to try a bit of a fun car bumper sticker design , I am open to other graphic elements .. this is just one and would fit in with part B of the brief below. If your designing a part A sticker then you would use the icon graphic or parts of the icon graphic for part B

We have a current brand that is represented by the blue and back icon with the white man and the word BLUEFOX We are looking for two styles of design submissions:

A) Designs that promote the new 1300BLUEFOX but also tie in with the current brand either with colour alone or by incorporating the icon graphic or both.

B) Designs that simply promote 1300BLUEFOX and have no tie to the current brand.

Submissions can target either A or B but those that contain designs for both A and B will be looked on more favourably.

```html
<!DOCTYPE html>
<html lang="en">
<head>
<meta charset="utf-8">
<title>1300BLUEFOX sticker</title>
<link rel="stylesheet" href="https://fonts.googleapis.com/css2?family=Roboto+Condensed:wght@700;800&display=swap">
<style>
  :root {
    --bg: #d9d9d9;
    --paper: #ffffff;
    --navy: #0f1a2e;
    --pink: #e8174f;
    --green: #5db547;
    --pill: #c4e6fb;
  }
  html, body {
    margin: 0;
    width: 1200px;
    height: 1000px;
    overflow: hidden;
    background: var(--bg);
    font-family: "Roboto Condensed", "Arial Narrow", sans-serif;
  }
  .canvas { position: relative; width: 1200px; height: 1000px; }
  .sticker-shape { position: absolute; left: 0; top: 0; }
  .call-now {
    position: absolute; left: 211px; top: 392px;
    margin: 0; font-size: 56px; font-weight: 700; color: var(--navy);
    line-height: 1; letter-spacing: -0.5px;
  }
  .headline {
    position: absolute; left: 203px; top: 440px;
    margin: 0; font-weight: 800; line-height: 1; white-space: nowrap;
  }
  .headline .digits { font-size: 150px; color: var(--pink); letter-spacing: -6px; }
  .headline .word { font-size: 96px; color: var(--navy); margin-left: 14px; letter-spacing: -1px; }
  .freefall-figure {
    position: absolute; left: 483px; top: 395px; width: 232px; height: 92px;
    border-radius: 46px;
    background: linear-gradient(90deg, rgba(15,26,46,0.15), rgba(15,26,46,0.55));
  }
  .web-address {
    position: absolute; left: 888px; top: 378px;
    font-size: 19px; font-weight: 700; color: var(--navy); letter-spacing: 0.2px;
  }
  .phone-pill {
    position: absolute; left: 852px; top: 502px; width: 232px; height: 50px;
    border-radius: 25px; background: var(--pill);
    display: flex; align-items: center; justify-content: center;
    font-size: 33px; font-weight: 700; color: var(--navy);
  }
</style>
</head>
<body>
<div class="canvas">
  <svg class="sticker-shape" width="1200" height="1000" viewBox="0 0 1200 1000" aria-hidden="true">
    <defs>
      <linearGradient id="border-split" gradientUnits="userSpaceOnUse" x1="0" y1="350" x2="0" y2="606">
        <stop offset="0.5" stop-color="#e8174f"/>
        <stop offset="0.5" stop-color="#5db547"/>
      </linearGradient>
    </defs>
    <path d="M185 350 H1105 V605 H185 Q167 605 167 587 V530 C140 530 118 510 118 485 C118 460 140 440 167 440 V368 Q167 350 185 350 Z"
          fill="#ffffff" stroke="url(#border-split)" stroke-width="6"/>
    <circle cx="158" cy="485" r="37" fill="#5db547"/>
    <g fill="none" stroke="#ffffff" stroke-width="3" stroke-linecap="round">
      <path d="M162 476 a8 8 0 0 1 8 8"/>
      <path d="M163 467 a17 17 0 0 1 16 16"/>
    </g>
    <path d="M146 468 l6 -3 l6 10 l-4 4 q3 8 10 12 l4 -4 l10 6 l-3 6 q-4 4 -10 1 q-18 -9 -23 -26 q-1 -4 4 -6 z" fill="#ffffff"/>
  </svg>

  <p class="call-now">Call NOW</p>
  <h1 class="headline"><span class="digits">1300</span><span class="word">BLUEFOX</span></h1>
  <div class="freefall-figure" role="img" aria-label="Silhouette of a skydiver in freefall, arms spread"></div>
  <div class="web-address">WWW.1300BLUEFOX.COM</div>
  <div class="phone-pill">1300 482 615</div>
</div>
</body>
</html>
```